Web Design for Financial Consulting Company

We need a website design for a financial consulting company "Kelvane Consulting". We build financial models, scenario analysis, handle the budgeting process and provide temporary staffing. I have over 10 years of experience. My Excel expertise and analytical savvy has saved clients over $17 million in profit.

Target Market(s)

Small to medium businesses

Industry/Entity Type

Financial Consulting

Number of Pages Required

4 page

Requirements
Must have
• Professional looking
Nice to have
• A little futuristic looking

```html
<!DOCTYPE html>
<html lang="en">
<head>
<meta charset="utf-8">
<title>Kelvane Consulting</title>
<link href="https://fonts.googleapis.com/css2?family=Figtree:wght@400;500;600;700&family=Roboto+Condensed:wght@700&display=swap" rel="stylesheet">
<style>
:root{
  --navy:#0a4673;
  --navy-deep:#073a62;
  --sky:#00a6ec;
  --sky-soft:#e3f5fd;
  --ink:#1b2633;
  --body:#3c4651;
  --paper:#ffffff;
  --mist:#f5f5f5;
  --star:#f7a21b;
}
*{margin:0;padding:0;box-sizing:border-box}
html,body{width:1200px;height:3602px;overflow:hidden}
body{position:relative;background:var(--paper);font-family:"Figtree",Arial,sans-serif;color:var(--body)}
.abs{position:absolute}

/* brand */
.brand{display:flex;align-items:center;gap:12px;color:var(--paper);font-weight:700;font-size:34px;letter-spacing:1px;text-transform:uppercase}
.brand-mark{width:40px;height:40px;border:5px solid var(--sky)}

/* hero */
.hero-edge{left:0;top:0;width:1200px;height:610px;background:var(--sky);clip-path:polygon(0 0,100% 0,100% 508px,0 606px)}
.hero{left:0;top:0;width:1200px;height:602px;clip-path:polygon(0 0,100% 0,100% 502px,0 598px);
  background:linear-gradient(100deg,#0c4f80 0%,#1a6796 35%,#6f8ea6 60%,#3d6a8e 100%)}
.hero-photo{left:0;top:0;width:1200px;height:602px}
.nav{top:34px;right:101px;display:flex;align-items:center;gap:0}
.nav a{color:var(--paper);text-decoration:none;font-size:15px;font-weight:500;padding:0 25px}
.nav a.cta{background:var(--sky);padding:15px 21px;margin-left:6px;color:var(--navy-deep)}
.hero-title{left:101px;top:196px;font-family:"Roboto Condensed",Arial,sans-serif;font-size:46px;line-height:66px;color:var(--paper);font-weight:700}
.btn{display:inline-block;font-size:16px;text-decoration:none}
.hero-btn{left:98px;top:416px;width:120px;height:46px;line-height:46px;text-align:center;background:var(--sky);color:var(--navy-deep)}

/* about */
.about-frame{left:99px;top:645px;width:120px;height:120px;border:8px solid var(--sky)}
.about-photo{left:155px;top:699px;width:518px;height:585px;background:linear-gradient(160deg,#3d4a52,#7d8a90 45%,#2b3338)}
.about-block{left:494px;top:1040px;width:606px;height:300px;background:var(--sky)}
.about-card{left:613px;top:735px;width:437px;height:507px;background:var(--paper);box-shadow:0 4px 24px rgba(0,0,0,.08);padding:74px 20px 0 19px}
.eyebrow{font-size:20px;color:var(--navy);font-weight:500}
.about-card h2{font-size:29px;font-weight:500;color:var(--navy);letter-spacing:.5px;margin-top:2px}
.about-card h2 span,.section-title span{color:var(--sky)}
.about-card p{font-size:15px;line-height:28px;margin-top:10px}
.about-card p + p{margin-top:0}
.about-card .callout{color:var(--sky);font-size:18px;line-height:29px;margin-top:0}
.read-more{margin-top:16px;width:139px;height:51px;line-height:51px;text-align:center;background:var(--navy);color:var(--sky);font-size:19px}

/* services */
.services{left:0;top:1428px;width:1200px;height:854px;background:var(--mist)}
.services-head{left:266px;top:1516px;color:var(--navy)}
.services-head .eyebrow{font-size:20px;line-height:22px}
.section-title{font-size:37px;font-weight:600;letter-spacing:1px;line-height:40px}
.band{left:97px;top:1716px;width:1003px;height:202px;background:var(--navy)}
.svc{background:var(--paper);box-shadow:0 4px 20px rgba(0,0,0,.06);padding:33px 16px 0 17px}
.svc-icon{width:80px;height:76px;background:var(--sky);display:flex;align-items:center;justify-content:center}
.svc h3{font-size:18px;font-weight:600;color:var(--ink);margin-top:28px}
.svc p{font-size:15px;line-height:28px;margin-top:10px;color:var(--body)}
.contact-today{left:858px;top:2156px;width:242px;height:64px;background:var(--navy);color:var(--sky);display:flex;align-items:center;justify-content:center;gap:12px;font-size:20px}

/* testimonial */
.test-photo{left:504px;top:2367px;width:592px;height:665px;background:linear-gradient(150deg,#9fb8cc,#5b7d99 40%,#223d5a 80%,#142637)}
.avatar{left:120px;top:2454px;width:188px;height:188px;border-radius:50%;border:2px solid var(--navy);background:radial-gradient(circle,#dfe4e8,#b9c3cb)}
.quote-card{left:101px;top:2664px;width:564px;height:258px;background:var(--paper);box-shadow:0 4px 24px rgba(0,0,0,.08);padding:26px 22px}
.quote-card p{font-size:15px;line-height:28px}
.quote-name{color:var(--navy);font-size:16px;font-weight:600;margin-top:20px}
.stars{color:var(--star);font-size:16px;letter-spacing:1px;margin-top:4px}
.quote-mark{right:20px;top:100px;font-size:140px;line-height:140px;color:#e6e6e6;font-family:Georgia,serif}
.dots{left:126px;top:2938px;display:flex;gap:12px}
.dots span{width:25px;height:4px;background:var(--sky)}
.dots span.on{background:var(--navy)}

/* footer */
.footer-edge{left:0;top:3150px;width:1200px;height:452px;background:var(--sky);clip-path:polygon(0 98px,100% 0,100% 100%,0 100%)}
.footer{left:0;top:3150px;width:1200px;height:452px;background:var(--navy-deep);clip-path:polygon(0 104px,100% 6px,100% 100%,0 100%)}
.footer-brand{left:0;width:1200px;top:3282px;justify-content:center;font-size:32px}
.footer-nav{left:0;width:1200px;top:3355px;display:flex;justify-content:center;gap:50px}
.footer-nav a{color:var(--paper);font-size:15px;font-weight:500;text-decoration:none}
.footer-rule{left:97px;top:3402px;width:1003px;height:1px;background:rgba(255,255,255,.2)}
.contact-item{top:3440px;display:flex;align-items:center;gap:12px;color:var(--paper);font-size:14px;line-height:20px}
.contact-icon{width:52px;height:52px;background:var(--sky);display:flex;align-items:center;justify-content:center}
.contact-item strong{display:block;font-size:16px;font-weight:600}
.copyright{left:0;width:1200px;top:3552px;text-align:center;color:var(--paper);font-size:14px}
</style>
</head>
<body>

<!-- hero -->
<div class="abs hero-edge"></div>
<div class="abs hero">
  <div class="abs hero-photo" role="img" aria-label="Smiling consultant in a suit talking with a client at an office desk"></div>
</div>
<div class="abs brand" style="left:98px;top:34px"><span class="brand-mark"></span>Kelvane Consulting</div>
<nav class="abs nav">
  <a href="#">Home</a><a href="#">About Us</a><a href="#">Services</a><a href="#" class="cta">Contact Us</a>
</nav>
<h1 class="abs hero-title">Helping Your Finance<br>Team And Increasing<br>Profit</h1>
<a href="#" class="abs btn hero-btn">Contact Us</a>

<!-- about -->
<div class="abs about-frame"></div>
<div class="abs about-photo" role="img" aria-label="Business team meeting around a table in front of a screen showing charts"></div>
<div class="abs about-block"></div>
<div class="abs about-card">
  <div class="eyebrow">About</div>
  <h2>KELVANE <span>CONSULTING</span></h2>
  <p>Lorem ipsum dolor sit amet, consectetuer adipiscing elit, sed diam nonummy nibh euismod tincidunt ut lor laoreet dolore magna aliquam erat volutpat. Ut wisilo ad minim veniam, quis.</p>
  <p>Our courteous, professional team is able to support a range of services to meet your requirements.</p>
  <p class="callout">To Learn More About Kelvane Consulting Services, Please Call Us At 123.456.7890</p>
  <a href="#" class="btn read-more">Read More</a>
</div>

<!-- services -->
<div class="abs services"></div>
<div class="abs services-head">
  <div class="eyebrow">What We Do</div>
  <div class="section-title">OUR <span>SERVICES</span></div>
</div>
<div class="abs band"></div>

<div class="abs svc" style="left:256px;top:1604px;width:326px;height:262px">
  <div class="svc-icon"><svg width="48" height="48" viewBox="0 0 48 48" fill="none" stroke="#fff" stroke-width="2"><rect x="4" y="18" width="12" height="12"/><rect x="30" y="6" width="12" height="10"/><rect x="30" y="20" width="12" height="10"/><rect x="30" y="34" width="12" height="10"/><path d="M16 24h7M23 11v28M23 11h7M23 25h7M23 39h7"/></svg></div>
  <h3>Financial Models Projects</h3>
  <p>Lorem ipsum dolor sit ameonsectetuer adipiscing elit, sed diam noummy nibh euismod tincidunt laoreet.</p>
</div>
<div class="abs svc" style="left:623px;top:1516px;width:326px;height:276px">
  <div class="svc-icon"><svg width="48" height="48" viewBox="0 0 48 48" fill="none" stroke="#fff" stroke-width="2"><circle cx="24" cy="12" r="8"/><path d="M24 8v8M21 10h5M21 14h5M24 20v6M10 26h28M10 26v6M24 26v6M38 26v6"/><rect x="5" y="32" width="10" height="9"/><rect x="19" y="32" width="10" height="9"/><rect x="33" y="32" width="10" height="9"/></svg></div>
  <h3>Budgeting Process</h3>
  <p>Lorem ipsum dolor sit ameonsectetuer adipiscing elit, sed diam noummy nibh euismod tincidunt laoreet.</p>
</div>
<div class="abs svc" style="left:97px;top:1919px;width:319px;height:275px">
  <div class="svc-icon"><svg width="50" height="50" viewBox="0 0 50 50" fill="none" stroke="#fff" stroke-width="2"><circle cx="13" cy="12" r="5"/><circle cx="25" cy="12" r="5"/><circle cx="37" cy="12" r="5"/><circle cx="25" cy="30" r="10"/><circle cx="25" cy="30" r="4"/><path d="M6 22h38M25 40v6M15 30H9M41 30h-6"/></svg></div>
  <h3>Temporary Staffing</h3>
  <p>Lorem ipsum dolor sit ameonsectetuer adipiscing elit, sed diam noummy nibh euismod tincidunt laoreet.</p>
</div>
<div class="abs svc" style="left:440px;top:1903px;width:317px;height:264px">
  <div class="svc-icon"><svg width="48" height="48" viewBox="0 0 48 48" fill="none" stroke="#fff" stroke-width="2"><ellipse cx="20" cy="9" rx="13" ry="4"/><path d="M7 9v26c0 2 6 4 13 4M33 9v12M7 18c0 2 6 4 13 4s13-2 13-4M7 27c0 2 6 4 13 4"/><rect x="27" y="28" width="14" height="14"/><path d="M31 35l3 3 5-6"/></svg></div>
  <h3>Data Cleansing</h3>
  <p>Lorem ipsum dolor sit ameonsectetuer adipiscing elit, sed diam noummy nibh euismod tincidunt laoreet.</p>
</div>
<div class="abs svc" style="left:783px;top:1844px;width:317px;height:274px">
  <div class="svc-icon"><svg width="50" height="50" viewBox="0 0 50 50" fill="none" stroke="#fff" stroke-width="2"><circle cx="25" cy="25" r="18"/><circle cx="25" cy="7" r="3"/><circle cx="25" cy="43" r="3"/><circle cx="7" cy="25" r="3"/><circle cx="43" cy="25" r="3"/><path d="M18 30v-6M23 30v-9M28 30v-7M33 30v-11"/></svg></div>
  <h3>Process Improvement</h3>
  <p>Lorem ipsum dolor sit ameonsectetuer adipiscing elit, sed diam noummy nibh euismod tincidunt laoreet.</p>
</div>
<a href="#" class="abs contact-today">
  <svg width="28" height="28" viewBox="0 0 24 24" fill="none" stroke="currentColor" stroke-width="1.6"><path d="M5 3h4l2 5-3 2a11 11 0 0 0 6 6l2-3 5 2v4a2 2 0 0 1-2 2A17 17 0 0 1 3 5a2 2 0 0 1 2-2z"/><path d="M15 3a6 6 0 0 1 6 6M15 7a2 2 0 0 1 2 2"/></svg>
  Contact Us Today
</a>

<!-- testimonial -->
<div class="abs test-photo" role="img" aria-label="Hand touching a tablet with glowing bar chart graphics rising from the screen"></div>
<div class="abs avatar" role="img" aria-label="Portrait of a client"></div>
<div class="abs quote-card">
  <p>Lorem ipsum dolor sit amet, consectetuer adipiscing elit, sed diam nonummy nibh euismod tincidunt ut laoreet dolore mag aliqLorem ipsum dolor sit amet, consectetuer adipising elit, sed diam nonummy nibh euismod tincidunt ut laoreet dolore agna aliquam erat volutpat. Ut wisi enici tation ullamcorper suscipit.</p>
  <div class="quote-name">Marla T.</div>
  <div class="stars">★★★★★</div>
  <div class="abs quote-mark">”</div>
</div>
<div class="abs dots"><span></span><span></span><span class="on"></span><span></span><span></span></div>

<!-- footer -->
<div class="abs footer-edge"></div>
<div class="abs footer"></div>
<div class="abs brand footer-brand"><span class="brand-mark"></span>Kelvane Consulting</div>
<nav class="abs footer-nav"><a href="#">Home</a><a href="#">About Us</a><a href="#">Services</a><a href="#">Contact Us</a></nav>
<div class="abs footer-rule"></div>

<div class="abs contact-item" style="left:112px">
  <div class="contact-icon"><svg width="28" height="28" viewBox="0 0 24 24" fill="none" stroke="#fff" stroke-width="1.6"><path d="M5 3h4l2 5-3 2a11 11 0 0 0 6 6l2-3 5 2v4a2 2 0 0 1-2 2A17 17 0 0 1 3 5a2 2 0 0 1 2-2z"/></svg></div>
  <div><strong>Phone</strong>123.456.7890</div>
</div>
<div class="abs contact-item" style="left:397px">
  <div class="contact-icon"><svg width="28" height="28" viewBox="0 0 24 24" fill="none" stroke="#fff" stroke-width="1.6"><path d="M12 22s7-7 7-12a7 7 0 0 0-14 0c0 5 7 12 7 12z"/><circle cx="12" cy="10" r="2.5"/></svg></div>
  <div>123 Ipsum Dolor Sit Am Constuer<br>Adipiscing Elit Sed Diam.</div>
</div>
<div class="abs contact-item" style="left:819px">
  <div class="contact-icon"><svg width="28" height="28" viewBox="0 0 24 24" fill="none" stroke="#fff" stroke-width="1.6"><rect x="3" y="6" width="18" height="13"/><path d="M3 6l9 7 9-7"/></svg></div>
  <div><strong>Email</strong>info@kelvaneconsulting.com</div>
</div>
<div class="abs copyright">© 2023 Kelvane Consulting. All Rights Reserved.</div>

</body>
</html>
```